Hair salon and Nail salon in Hawaii need a newspaper Ad design.

We need a newspaper Ad design for new open hair & nail salon in Waikiki Hawaii.Our Recommendation service for hair is "Head Spa" $30+tax and for nail is "Manicure Treatment Course" (Filing+Cuticle Care+Massage+Coloring) $20+tax.
We would like to see Hawaiian taste color and also having sense of luxury design. The ad size is W 5.0” x H 6.375”.
I would customers to know the shop place(Lanakila Crest Hotel 1F) , phone(808-555-0173), instagram(salonbrightwave) , our web site https://salonbrightwave.example and recommend services. For Web or Instagram , QR code is acceptable.

Target Market(s)

women & men

Industry/Entity Type

Beauty Salon

Font styles to use
Serif

Colors

Designer to choose colors to be used in the design.

Requirements
Must have
• Tagline for local customers. Shop Name is "SALON BRIGHTWAVE".the shop place(Lanakila Crest Hotel 1F) , phone(808-555-0173), instagram(salonbrightwave) and recommend services.
Nice to have
• Our services are competitive, but we don't want to be seen as just cheap and low quality.

```html
<!DOCTYPE html>
<html lang="en">
<head>
<meta charset="utf-8">
<title>Salon Brightwave – Newspaper Ad</title>
<link rel="stylesheet" href="https://fonts.googleapis.com/css2?family=Fira+Sans:wght@300;400;500;600;700&display=swap">
<style>
  :root {
    --sand-light: #ecd2ad;
    --sand-deep: #d7b289;
    --ink-teal: #0f3140;
    --sunset-orange: #e2561b;
    --hibiscus-gold: #e6ae17;
    --coral: #ef5d4c;
    --paper: #ffffff;
    --text-dark: #15303c;
  }
  * { box-sizing: border-box; margin: 0; padding: 0; }
  html, body { width: 1200px; height: 900px; overflow: hidden; background: #ffffff; }
  .ad {
    position: relative;
    width: 1200px;
    height: 900px;
    overflow: hidden;
    font-family: "Fira Sans", sans-serif;
    color: var(--text-dark);
    background: linear-gradient(160deg, var(--sand-light) 0%, var(--sand-deep) 100%);
  }
  .hero-photo {
    position: absolute;
    left: 0; top: 0;
    width: 640px; height: 600px;
    background: radial-gradient(ellipse at 45% 30%, #6b3f25 0%, #8c5a3a 35%, rgba(200,160,120,0.6) 65%, rgba(215,178,137,0) 85%);
  }
  .waves { position: absolute; inset: 0; width: 1200px; height: 900px; }
  .brand {
    position: absolute;
    right: 112px; top: 62px;
    display: flex; flex-direction: column; align-items: center; gap: 12px;
  }
  .brand-mark {
    width: 92px; height: 92px; border-radius: 50%;
    background: var(--paper);
  }
  .brand-name { font-size: 29px; font-weight: 300; color: var(--text-dark); letter-spacing: 0.5px; }
  .headline {
    position: absolute; right: 90px; top: 230px;
    text-align: right; font-weight: 400; line-height: 1.3;
  }
  .headline-lead { font-size: 43px; color: var(--text-dark); }
  .headline-accent { font-size: 43px; color: var(--sunset-orange); }
  .headline-accent strong { font-weight: 700; }
  .detail-photo {
    position: absolute;
    left: 318px; top: 453px;
    width: 268px; height: 268px; border-radius: 50%;
    border: 9px solid var(--ink-teal);
    background: radial-gradient(circle at 50% 40%, #f1ddd0 0%, #d9b9a3 55%, #c9a58c 100%);
  }
  .intro {
    position: absolute; right: 102px; top: 494px;
    text-align: right; font-size: 21px; line-height: 1.35; color: var(--text-dark);
  }
  .service-tag {
    position: absolute; left: 729px; top: 577px;
    width: 363px; height: 50px; border-radius: 25px;
    background: var(--coral); color: var(--paper);
    font-size: 24px; font-weight: 600;
    display: flex; align-items: center; justify-content: center;
    box-shadow: 0 10px 10px -6px rgba(0,0,0,0.35);
  }
  .service-list { position: absolute; left: 560px; top: 655px; width: 540px; font-size: 22px; color: var(--text-dark); }
  .service-item { position: absolute; white-space: nowrap; }
  .service-item .price { font-weight: 500; }
  .item-headspa { left: 85px; top: 0; }
  .item-manicure-name { left: 14px; top: 44px; }
  .item-manicure-detail { left: 0; top: 74px; }
  .item-manicure-price { left: 0; top: 104px; }
  .flora {
    position: absolute; right: 0; bottom: 0;
    width: 380px; height: 300px;
  }
  .contact {
    position: absolute; left: 48px; top: 720px;
    list-style: none; font-size: 22px; font-weight: 600; color: var(--text-dark);
  }
  .contact li { display: flex; align-items: center; gap: 14px; height: 33px; }
  .contact svg { width: 20px; height: 20px; flex: none; }
  .social { position: absolute; left: 288px; top: 830px; display: flex; gap: 18px; }
  .social span { width: 26px; height: 26px; border-radius: 50%; border: 3px solid var(--text-dark); }
</style>
</head>
<body>
<main class="ad">
  <div class="hero-photo" role="img" aria-label="Photo of a smiling woman with voluminous curly hair"></div>

  <svg class="waves" viewBox="0 0 1200 900" aria-hidden="true">
    <rect x="56" y="48" width="1086" height="814" fill="none" stroke="var(--ink-teal)" stroke-width="2.5"/>
    <path d="M0,470 C300,520 600,430 900,380 C1000,365 1100,370 1200,375 L1200,420 C900,420 600,520 0,560 Z" fill="#ffffff" opacity="0.35"/>
    <path d="M0,530 C180,560 320,540 460,470 C640,380 950,350 1200,380 L1200,900 L0,900 Z" fill="var(--ink-teal)"/>
    <path d="M0,595 C200,655 360,640 500,545 C660,430 950,395 1200,398 L1200,900 L0,900 Z" fill="var(--sunset-orange)"/>
    <path d="M0,622 C200,690 380,680 520,572 C680,452 950,412 1200,412 L1200,900 L0,900 Z" fill="var(--hibiscus-gold)"/>
    <path d="M385,900 C420,760 500,565 700,492 C850,442 1000,432 1200,432 L1200,900 Z" fill="var(--paper)"/>
    <path d="M1142,440 L1142,862 L470,862" fill="none" stroke="var(--hibiscus-gold)" stroke-width="2.5"/>
  </svg>

  <div class="brand">
    <span class="brand-mark"></span>
    <span class="brand-name">salonbrightwave</span>
  </div>

  <h1 class="headline">
    <span class="headline-lead">Are you ready for a</span><br>
    <span class="headline-accent">NEW &amp; BETTER <strong>YOU?</strong></span>
  </h1>

  <div class="detail-photo" role="img" aria-label="Close-up photo of manicured hand with a tropical flower"></div>

  <p class="intro">Our newly opened Hair and Nail salon<br>now in Waikiki, Hawaii</p>

  <div class="service-tag">Our Recommended Service</div>

  <div class="service-list">
    <p class="service-item item-headspa">Head Spa.......................................... <span class="price">$30+tax</span></p>
    <p class="service-item item-manicure-name">Manicure Treatment Course</p>
    <p class="service-item item-manicure-detail">(Filing+Cuticle Care+Massage+Coloring)</p>
    <p class="service-item item-manicure-price">.............................................................................. <span class="price">$20+tax</span></p>
  </div>

  <svg class="flora" viewBox="0 0 380 300" role="img" aria-label="Watercolor illustration of tropical palm leaves and hibiscus flowers">
    <defs>
      <linearGradient id="floraTone" x1="0" y1="1" x2="1" y2="0">
        <stop offset="0" stop-color="#8fbf5a" stop-opacity="0.75"/>
        <stop offset="0.55" stop-color="#f39a78" stop-opacity="0.8"/>
        <stop offset="1" stop-color="#f4b35c" stop-opacity="0.7"/>
      </linearGradient>
    </defs>
    <path d="M20,300 C70,255 160,232 258,226 C262,160 280,100 312,58 C335,30 360,14 380,6 L380,300 Z" fill="url(#floraTone)"/>
  </svg>

  <ul class="contact">
    <li><svg viewBox="0 0 24 24"><path d="M12 2a7 7 0 0 0-7 7c0 5 7 13 7 13s7-8 7-13a7 7 0 0 0-7-7zm0 9.5A2.5 2.5 0 1 1 12 6.5a2.5 2.5 0 0 1 0 5z" fill="var(--text-dark)"/></svg>Lanakila Crest Hotel 1F</li>
    <li><svg viewBox="0 0 24 24"><path d="M6.6 10.8a15 15 0 0 0 6.6 6.6l2.2-2.2a1 1 0 0 1 1-.25 11.4 11.4 0 0 0 3.6.57 1 1 0 0 1 1 1V20a1 1 0 0 1-1 1A17 17 0 0 1 3 4a1 1 0 0 1 1-1h3.5a1 1 0 0 1 1 1c0 1.250.2 2.45.57 3.57a1 1 0 0 1-.25 1z" fill="var(--text-dark)"/></svg>808-555-0173</li>
    <li><svg viewBox="0 0 24 24"><circle cx="12" cy="12" r="9" fill="none" stroke="var(--text-dark)" stroke-width="2"/><path d="M3 12h18M12 3c3 3 3 15 0 18M12 3c-3 3-3 15 0 18" fill="none" stroke="var(--text-dark)" stroke-width="1.6"/></svg>www.salonbrightwave.example</li>
  </ul>

  <div class="social" aria-hidden="true"><span></span><span></span></div>
</main>
</body>
</html>
```